Cover for Where the Quiet River Bends Beyond Our Morning

Cover for a book that describes everything that happens to a person, from pre-birth life plans through growing in compassion and wisdom to death and living in the afterlife. The information is revealed in messages from people living in the life after this life. The title is Lanterns Along the Hidden Stair of Every Soul: Gathered from Voices Dwelling in the Further Meadow. Author is T. Morven Ashdale. Book size is 6 by 9.

Target Market(s)

General

Font styles to use
Serif

```html
<!DOCTYPE html>
<html lang="en">
<head>
<meta charset="utf-8">
<title>Where the Quiet River Bends Beyond Our Morning — Cover</title>
<link rel="stylesheet" href="https://fonts.googleapis.com/css2?family=Cormorant+Garamond:wght@500&family=EB+Garamond:wght@400;500&family=Tinos&display=swap">
<style>
  :root {
    --page-bg: #eeeeee;
    --paper: #ffffff;
    --ink: #1a1a1a;
    --teal: #1f5f86;
    --leaf: #4f7a35;
    --ornament: #2b6d92;
  }
  html, body {
    margin: 0;
    padding: 0;
    width: 899px;
    height: 1200px;
    overflow: hidden;
    background: var(--page-bg);
  }
  .spread {
    position: absolute;
    left: 19px;
    top: 302px;
    width: 860px;
    height: 595px;
    background: var(--paper);
    box-shadow: 0 2px 8px rgba(0,0,0,0.18);
    color: var(--ink);
  }
  .butterfly {
    position: absolute;
    border-radius: 40% 50% 30% 45%;
    background: linear-gradient(135deg, var(--teal) 0%, #2f7a6a 50%, var(--leaf) 100%);
    opacity: 0.85;
  }
  /* Back cover */
  .back-butterfly { left: 155px; top: 52px; width: 84px; height: 76px; }
  .blurb {
    position: absolute;
    left: 35px;
    top: 160px;
    width: 334px;
    font-family: "Tinos", serif;
    font-size: 8.4px;
    line-height: 10.4px;
    text-align: justify;
    hyphens: auto;
  }
  .blurb p { margin: 0 0 10px; }
  /* Spine */
  .spine-title {
    position: absolute;
    left: 431px;
    top: 36px;
    width: 18px;
    height: 390px;
    writing-mode: vertical-rl;
    font-family: "Tinos", serif;
    font-size: 14.5px;
    white-space: nowrap;
    text-align: center;
  }
  .spine-butterfly { left: 414px; top: 434px; width: 22px; height: 22px; }
  .spine-author {
    position: absolute;
    left: 440px;
    top: 470px;
    writing-mode: vertical-rl;
    transform: rotate(180deg);
    font-family: "EB Garamond", serif;
    font-size: 7px;
    letter-spacing: 2.5px;
    white-space: nowrap;
  }
  /* Front cover */
  .front {
    position: absolute;
    left: 470px;
    top: 0;
    width: 390px;
    height: 595px;
    text-align: center;
  }
  .tagline {
    position: absolute;
    top: 46px;
    left: 0;
    width: 100%;
    margin: 0;
    font-family: "EB Garamond", serif;
    font-weight: 500;
    font-size: 11.5px;
    line-height: 15px;
    letter-spacing: 2.2px;
    text-transform: uppercase;
  }
  .front-butterfly { left: 143px; top: 162px; width: 86px; height: 86px; }
  .ornament {
    position: absolute;
    left: 136px;
    width: 110px;
    height: 4px;
    background: var(--ornament);
    border-radius: 2px;
  }
  .ornament-top { top: 320px; }
  .ornament-bottom { top: 486px; }
  .title {
    position: absolute;
    top: 340px;
    left: 0;
    width: 382px;
    margin: 0;
    font-family: "Cormorant Garamond", serif;
    font-weight: 500;
    font-size: 28px;
    line-height: 32px;
  }
  .title span { display: block; }
  .author {
    position: absolute;
    top: 530px;
    left: 0;
    width: 382px;
    margin: 0;
    font-family: "EB Garamond", serif;
    font-weight: 400;
    font-size: 16px;
    letter-spacing: 5px;
    text-transform: uppercase;
  }
</style>
</head>
<body>
  <main class="spread">
    <section class="back-cover">
      <div class="butterfly back-butterfly" role="img" aria-label="Teal-to-green butterfly illustration"></div>
      <div class="blurb">
        <p>Before you were born, you helped choose the people, places and trials that would shape this life. Speakers who now dwell beyond the veil describe how those plans are made, why hardship so often arrives with purpose, and how every encounter offers a chance to grow in compassion and wisdom. Their messages, gathered over many years of careful sessions, explain what the soul feels at the moment of passing, who waits to greet it, and how it reviews the life just lived without judgment or fear. They speak of homes, gardens and studies in the further meadow, of loved ones who remain close, and of the quiet work of helping those still on earth. Each chapter follows one part of the journey, from the first decision to be born through childhood, love, loss and old age, then onward into a life that continues with joy, learning and renewed purpose.</p>
        <p>Written for anyone who has wondered why things happen as they do, this book offers comfort to the grieving, calm to the anxious and a clear map for the road ahead. Read it slowly, one chapter at a time, and let the voices speak for themselves.</p>
      </div>
    </section>

    <section class="spine">
      <div class="spine-title">Where the Quiet River Bends Beyond Our Morning</div>
      <div class="butterfly spine-butterfly" role="img" aria-label="Small green butterfly illustration"></div>
      <div class="spine-author">T. Morven Ashdale</div>
    </section>

    <section class="front">
      <p class="tagline">Entities speaking from the afterlife<br>have revealed</p>
      <div class="butterfly front-butterfly" role="img" aria-label="Teal-to-green butterfly illustration"></div>
      <div class="ornament ornament-top" role="img" aria-label="Blue flourish divider"></div>
      <h1 class="title">
        <span>Where the Quiet</span>
        <span>River Bends</span>
        <span>Beyond Our</span>
        <span>Morning</span>
      </h1>
      <div class="ornament ornament-bottom" role="img" aria-label="Blue flourish divider"></div>
      <p class="author">T. Morven Ashdale</p>
    </section>
  </main>
</body>
</html>
```